https://dorvakel.com

We need a cool technology design for our Managed IT Services company. We are located in Coral Springs Florida. We provide all IT services and support for small to medium sized businesses. We would like to see designs that use our blue and white colors from our website.

```html
<!DOCTYPE html>
<html lang="en">
<head>
<meta charset="utf-8">
<title>Dorvakel Business Card</title>
<link href="https://fonts.googleapis.com/css2?family=Work+Sans:wght@400;500;600&display=swap" rel="stylesheet">
<style>
  :root {
    --backdrop: #111418;
    --card: #1d2127;
    --card-edge: #272c33;
    --brand-blue: #2f8fe0;
    --brand-blue-soft: #5aa9ee;
    --ink: #f4f6f8;
    --ink-soft: #d9dee4;
  }
  * { margin: 0; padding: 0; box-sizing: border-box; }
  html, body {
    width: 1200px;
    height: 900px;
    overflow: hidden;
    background: var(--backdrop);
    font-family: "Work Sans", Arial, sans-serif;
  }
  .canvas {
    position: relative;
    width: 1200px;
    height: 900px;
  }
  .card {
    position: absolute;
    left: 280px;
    width: 640px;
    height: 366px;
    background: linear-gradient(135deg, var(--card-edge), var(--card));
    box-shadow: 0 10px 30px rgba(0, 0, 0, 0.55);
    overflow: hidden;
  }
  .card--front { top: 60px; }
  .card--back { top: 470px; }
  .card__band {
    position: absolute;
    left: 0;
    bottom: 0;
    width: 100%;
    height: 6px;
    background: var(--brand-blue);
  }

  .wordmark {
    display: flex;
    align-items: center;
    gap: 14px;
    font-weight: 600;
    color: var(--ink);
    letter-spacing: 0.01em;
    white-space: nowrap;
  }
  .wordmark__dot {
    width: 18px;
    height: 18px;
    border-radius: 50%;
    background: var(--brand-blue);
    flex: none;
  }
  .card--front .wordmark {
    position: absolute;
    left: 0; right: 0; top: 0; bottom: 0;
    justify-content: center;
    font-size: 58px;
  }
  .card--back .wordmark {
    position: absolute;
    left: 48px;
    top: 150px;
    font-size: 40px;
    gap: 10px;
  }
  .card--back .wordmark__dot {
    width: 13px;
    height: 13px;
  }
  .divider {
    position: absolute;
    left: 322px;
    top: 86px;
    width: 2px;
    height: 196px;
    background: var(--brand-blue);
  }
  .contact {
    position: absolute;
    left: 350px;
    top: 88px;
    color: var(--ink);
  }
  .contact__name {
    font-size: 22px;
    font-weight: 500;
    letter-spacing: 0.14em;
    text-transform: uppercase;
  }
  .contact__role {
    font-size: 14px;
    color: var(--brand-blue-soft);
    margin-bottom: 16px;
  }
  .contact__address {
    font-size: 14px;
    line-height: 1.35;
    color: var(--ink-soft);
    margin-bottom: 10px;
  }
  .contact__line {
    display: flex;
    align-items: center;
    gap: 10px;
    font-size: 14px;
    line-height: 1.75;
    color: var(--ink-soft);
  }
  .contact__icon {
    width: 12px;
    height: 12px;
    flex: none;
  }
</style>
</head>
<body>
<main class="canvas">
  <section class="card card--front" aria-label="Card front">
    <div class="wordmark"><span class="wordmark__dot"></span>DORVAKEL</div>
    <div class="card__band"></div>
  </section>

  <section class="card card--back" aria-label="Card back">
    <div class="wordmark"><span class="wordmark__dot"></span>DORVAKEL</div>
    <div class="divider"></div>
    <div class="contact">
      <p class="contact__name">Daniel Corwin</p>
      <p class="contact__role">Founder</p>
      <p class="contact__address">2870 Palm Ridge Ave #140<br>Coral Springs, Florida 33071</p>
      <p class="contact__line">
        <svg class="contact__icon" viewBox="0 0 12 12" aria-hidden="true"><path d="M2.5 1 L4.5 1 L5.2 3.5 L4 4.5 Q5 7 7.5 8 L8.5 6.8 L11 7.5 L11 9.5 Q10 11 8 10.8 Q2 9.5 1 3.5 Q1 1.8 2.5 1 Z" fill="none" stroke="#5aa9ee" stroke-width="1"/></svg>
        (954) 555-0148
      </p>
      <p class="contact__line">
        <svg class="contact__icon" viewBox="0 0 12 12" aria-hidden="true"><rect x="0.8" y="2.3" width="10.4" height="7.4" fill="none" stroke="#5aa9ee" stroke-width="1"/><path d="M0.8 2.5 L6 6.5 L11.2 2.5" fill="none" stroke="#5aa9ee" stroke-width="1"/></svg>
        info@dorvakel.com
      </p>
      <p class="contact__line">
        <svg class="contact__icon" viewBox="0 0 12 12" aria-hidden="true"><circle cx="6" cy="6" r="5" fill="none" stroke="#5aa9ee" stroke-width="1"/><ellipse cx="6" cy="6" rx="2.2" ry="5" fill="none" stroke="#5aa9ee" stroke-width="1"/><path d="M1 6 H11" stroke="#5aa9ee" stroke-width="1"/></svg>
        www.dorvakel.com
      </p>
    </div>
    <div class="card__band"></div>
  </section>
</main>
</body>
</html>
```